Pages That Sell Services - book cover (front panel only)

I want a book cover (for print and ebook) in a distinctive, quirky style that can be repurposed for podcast artwork too. Full brief supplied.
The book is a practical, accessible handbook for anyone thinking about writing a book to build their business, with a wide range of tips and techniques to help plan, write, publishing and promote a book that’s integrated with your platform and works to build your reputation, network and credibility from day 1.
The target audience is experts in business, particularly owners of SMEs with an established online and offline platform (eg speaking, training, consulting) who want to add a book to take their business to the next level.
I want the design to be strong and distinctive, slightly quirky without being gimmicky, with the focus on typography.

Target Market(s)

Those writing a book based on their expertise to build their business

Industry/Entity Type

Publishing Company

Font styles to use
Serif
Sans Serif
Decorative

Colors

Designer to choose colors to be used in the design.

Requirements
Must have
• Commercially appealing book cover design, with application files and copyright supplied, front panel only, 5.5 x 8.5 inch format. Must work at both full size and thumbnail.
Nice to have
• A distinctive style that could be applied across other products in my portfolio.

```html
<!DOCTYPE html>
<html lang="en">
<head>
<meta charset="utf-8">
<title>Pages That Sell Services – Front Cover</title>
<link href="https://fonts.googleapis.com/css2?family=Crimson+Pro:ital,wght@0,700;1,400&family=Jost:wght@400&display=swap" rel="stylesheet">
<style>
  :root {
    --backdrop: #ececec;
    --paper: #ffffff;
    --ink: #1d1d1b;
    --highlighter: #ffec00;
    --highlighter-soft: #fff7a8;
    --trim: #2a2a2a;
  }
  html, body {
    margin: 0;
    width: 1200px;
    height: 800px;
    overflow: hidden;
    background: var(--backdrop);
  }
  .stage {
    position: relative;
    width: 1200px;
    height: 800px;
  }
  .cover {
    position: absolute;
    left: 360px;
    top: 30px;
    width: 479px;
    height: 740px;
    background: var(--paper);
    outline: 1px solid var(--trim);
    overflow: hidden;
  }
  .cover__artwork {
    position: absolute;
    left: 12px;
    top: 28px;
    width: 440px;
    height: 672px;
    background: radial-gradient(ellipse at 55% 45%, var(--paper) 0%, var(--highlighter-soft) 72%, var(--highlighter) 100%);
  }
  .cover__title {
    position: absolute;
    left: 50px;
    top: 92px;
    margin: 0;
    font-family: "Crimson Pro", "Palatino Linotype", serif;
    font-weight: 700;
    font-size: 100px;
    line-height: 100px;
    letter-spacing: -0.5px;
    color: var(--ink);
  }
  .cover__title span { display: block; }
  .cover__subtitle {
    position: absolute;
    left: 50px;
    top: 502px;
    width: 262px;
    margin: 0;
    font-family: "Jost", "Futura", sans-serif;
    font-weight: 400;
    font-size: 17.5px;
    line-height: 23px;
    color: var(--ink);
  }
  .cover__author {
    position: absolute;
    left: 48px;
    top: 634px;
    margin: 0;
    font-family: "Crimson Pro", "Palatino Linotype", serif;
    font-style: italic;
    font-weight: 400;
    font-size: 50px;
    line-height: 1;
    color: var(--ink);
  }
</style>
</head>
<body>
<main class="stage">
  <article class="cover">
    <div class="cover__artwork" role="img" aria-label="Hand-painted yellow brush outline of a book with a rising arrow drawn inside it"></div>
    <h1 class="cover__title">
      <span>Pages</span>
      <span>That</span>
      <span>Sell</span>
      <span>Services</span>
    </h1>
    <p class="cover__subtitle">Clever ways to plan and write a book that works harder for your business</p>
    <p class="cover__author">Helen Marsh</p>
  </article>
</main>
</body>
</html>
```